Construction material supplies company business card ****

1. Full company name “K R Mortar Works Ltd”
I am after a Business card design for the company as a whole. We are better known in Solomon Islands as “K R Mortar” for short.

We are a building materials supplier of
Ready Mixed Concrete, Bricks and Blocks,
Quarry products- gravel, aggregates, sand etc.
Cement distributor/retailer of reputable brands.
Other prefab concrete products. Culverts, wave breakers, concrete retaining blocks etc.

2. Competitive Advantage over Competition: Quality, efficient, professional, dependable, reliable

3. We want people to feel trust worthy, high quality, strong when they see our brand

5. No preference to color. Maybe more sturdy and corporate. Not fancy.

Industry/Entity Type

CONSTRUCTION SUPPLY

Contact Information for Business Card

Name, Position, office phone mob phone, email

Requirements
Must have
• the company logo
Nice to have
• would like to see a mixture of designs, of with logo only and also with simple graphic designs to bring out the company whilst still have the strong sturdy professional feeling

```html
<!DOCTYPE html>
<html lang="en">
<head>
<meta charset="utf-8">
<title>K R Mortar – Business Card</title>
<link rel="stylesheet" href="https://fonts.googleapis.com/css2?family=Saira:wght@600&family=Raleway:wght@400;700&family=Arimo:wght@400&display=swap">
<style>
  :root {
    --backdrop: #b0b0b0;
    --navy: #123a5e;
    --navy-deep: #0f3253;
    --paper: #efefef;
    --brand-light: #d6d9dd;
    --ink: #1b1b1b;
    --muted: #555555;
    --white: #ffffff;
  }
  * { margin: 0; padding: 0; box-sizing: border-box; }
  html, body { width: 1200px; height: 960px; overflow: hidden; }
  body { background: var(--backdrop); position: relative; font-family: "Arimo", Arial, sans-serif; }

  .card { position: absolute; width: 471px; height: 268px; overflow: hidden; }

  .card-front { left: 478px; top: 161px; background: var(--navy); }
  .card-front .brand-name {
    position: absolute; left: 266px; top: 100px;
    font-family: "Saira", sans-serif; font-weight: 600; font-size: 29px;
    letter-spacing: 1px; color: var(--brand-light); white-space: nowrap;
  }

  .card-back { left: 228px; top: 530px; background: var(--paper); }
  .card-back .brand-name {
    position: absolute; left: 16px; top: 70px;
    font-family: "Saira", sans-serif; font-weight: 600; font-size: 27px;
    letter-spacing: 1px; color: var(--navy); white-space: nowrap;
  }
  .holder { position: absolute; left: 16px; top: 137px; }
  .holder-name { font-family: "Raleway", sans-serif; font-weight: 700; font-size: 17px; color: var(--navy); }
  .holder-role { font-family: "Raleway", sans-serif; font-weight: 400; font-size: 10px; color: var(--muted); margin-top: 1px; }

  .contacts { position: absolute; left: 18px; top: 203px; list-style: none; }
  .contacts li { display: flex; align-items: center; height: 18px; font-size: 12px; color: var(--ink); }
  .contacts svg { width: 12px; height: 12px; margin-right: 10px; fill: var(--navy); flex: none; }

  .footer-line { position: absolute; left: 0; bottom: 0; width: 100%; height: 4px; background: var(--navy); }
  .web-band {
    position: absolute; right: 0; bottom: 0; width: 182px; height: 24px;
    background: var(--navy); clip-path: polygon(7px 0, 100% 0, 100% 100%, 0 100%);
  }
  .web-address {
    position: absolute; left: 22px; top: 5px;
    font-size: 12px; letter-spacing: 2px; color: var(--white); white-space: nowrap;
  }
</style>
</head>
<body>
  <section class="card card-front" aria-label="Card front">
    <div class="brand-name">K R MORTAR</div>
  </section>

  <section class="card card-back" aria-label="Card back">
    <div class="brand-name">K R MORTAR</div>

    <div class="holder">
      <div class="holder-name">Daniel Koroi</div>
      <div class="holder-role">Director</div>
    </div>

    <ul class="contacts">
      <li>
        <svg viewBox="0 0 24 24" aria-hidden="true"><path d="M6.6 10.8a15.1 15.1 0 0 0 6.6 6.6l2.2-2.2c.3-.3.7-.4 1-.2 1.1.4 2.3.6 3.6.6.6 0 1 .4 1 1V20c0 .6-.4 1-1 1A17 17 0 0 1 3 4c0-.6.4-1 1-1h3.5c.6 0 1 .4 1 1 0 1.3.2 2.5.6 3.6.1.3 0 .7-.2 1z"/></svg>
        555 210 4478
      </li>
      <li>
        <svg viewBox="0 0 24 24" aria-hidden="true"><path d="M7 1h10a2 2 0 0 1 2 2v18a2 2 0 0 1-2 2H7a2 2 0 0 1-2-2V3a2 2 0 0 1 2-2zm0 3v14h10V4zm5 15.5a1.2 1.2 0 1 0 0 2.4 1.2 1.2 0 0 0 0-2.4z"/></svg>
        555 210 4478
      </li>
      <li>
        <svg viewBox="0 0 24 24" aria-hidden="true"><path d="M2 5h20v14H2zm2 2v.5l8 5 8-5V7zm0 2.8V17h16V9.8l-8 5z"/></svg>
        info@krmortar.com
      </li>
    </ul>

    <div class="footer-line"></div>
    <div class="web-band"><span class="web-address">www.krmortar.com</span></div>
  </section>
</body>
</html>
```